Amber Heron Fund Pitch Deck

This is a PowerPoint for use in investor presentations. The copy is written (although it may have small tweaks) and the designer will be responsible for creating a template and some graphical representations inside the presentation.

Note on the logo. Only the Amber Heron should be used, not the text.

```html
<!DOCTYPE html>
<html lang="en">
<head>
<meta charset="utf-8">
<title>Amber Heron Fund Pitch Deck</title>
<link href="https://fonts.googleapis.com/css2?family=Ubuntu:wght@300;400;500;700&display=swap" rel="stylesheet">
<style>
:root{
  --blue:#6b8bcd;
  --blue-deep:#3f5ea8;
  --blue-soft:#a9bde6;
  --ink:#333842;
  --grey-bg:#d5d5d5;
  --scene-bg:#e4e7ec;
  --dark-box:#4a4a4a;
  --white:#ffffff;
}
*{box-sizing:border-box;margin:0;padding:0}
html,body{width:1200px;height:2448px;overflow:hidden}
body{font-family:"Ubuntu",sans-serif;color:var(--ink);background:var(--grey-bg);position:relative}
.hero{position:absolute;left:0;top:0;width:1200px;height:712px;background:linear-gradient(180deg,#eef0f4,var(--scene-bg))}
.hero-slide{position:absolute;left:240px;top:150px;transform:scale(1.281);transform-origin:0 0;box-shadow:0 10px 30px rgba(0,0,0,.18)}
.slide{position:absolute;width:562px;height:316px;background:var(--white);overflow:hidden}
.slide svg.bg{position:absolute;left:0;top:0}
.brand{position:absolute;display:flex;align-items:center;gap:6px;font-weight:500;color:var(--blue);letter-spacing:1.5px;text-transform:uppercase}
.brand .dot{width:9px;height:9px;border-radius:50%;background:currentColor}
.cover-brand{left:38px;top:58px;font-size:10px}
.cover-title{position:absolute;left:37px;top:128px;font-size:27px;line-height:30px;color:var(--blue);font-weight:400}
.cover-text{position:absolute;left:37px;top:197px;width:255px;font-size:7.6px;line-height:9px}
.date-pill{position:absolute;left:37px;top:248px;width:111px;height:15px;background:var(--blue);color:#fff;font-size:6.5px;line-height:15px;text-align:center}
.copyright{position:absolute;right:28px;top:284px;font-size:5.5px;color:#fff}
.cover-dark{background:var(--blue)}
.cover-dark .cover-title,.cover-dark .cover-text,.cover-dark .cover-brand{color:#fff}
.cover-dark .date-pill{background:var(--blue-deep)}
.cover-dark .copyright{color:#d5e0f6}
.foot-brand{left:12px;top:290px;font-size:7px;letter-spacing:.5px;text-transform:none}
.page-no{position:absolute;right:14px;top:292px;font-size:5px;color:var(--blue)}
.head{font-size:18px;color:var(--blue);font-weight:400}
.head b{font-weight:700}
.photo{position:absolute}
.edge-title{position:absolute;left:45px;top:40px}
.edge-text{position:absolute;left:45px;top:86px;width:255px;font-size:10px;line-height:11.5px}
.edge-band{position:absolute;left:0;top:178px;width:562px;height:80px;background:rgba(107,139,205,.92);color:#fff;font-size:10px;line-height:12px;padding:14px 80px 0 45px}
.tech-title{position:absolute;left:0;right:0;top:22px;text-align:center}
.tech-text{position:absolute;left:27px;top:193px;width:515px;font-size:9.3px;line-height:11px}
.tech-text p{margin-bottom:6px}
.people-panel{position:absolute;left:35px;top:0;width:150px;height:170px;background:linear-gradient(160deg,#8ba4d9,var(--blue));color:#fff;text-align:center;font-size:17px;line-height:20px;padding-top:80px}
.people-panel b{font-weight:700}
.name-bar{position:absolute;height:31px;background:var(--blue-soft);color:#fff;padding:4px 8px 0}
.name-bar.solid{background:var(--blue)}
.name-bar h3{font-size:11px;font-weight:400;line-height:12px}
.name-bar h3 b{font-weight:700}
.name-bar span{display:block;font-size:5.5px;margin-top:2px}
.bio{position:absolute;font-size:5px;line-height:6px;list-style:disc;padding-left:9px}
.bio li{margin-bottom:2px}
.market-panel{position:absolute;left:187px;top:17px;width:358px;height:255px;background:var(--blue)}
.market-title{position:absolute;left:25px;top:134px;line-height:19px}
.market-text{position:absolute;left:25px;top:182px;width:150px;font-size:7px;line-height:8px}
.market-text a{color:var(--blue-deep);font-size:5.5px}
.market-note{position:absolute;left:426px;top:166px;width:112px;text-align:center;color:#fff;font-size:7px;line-height:8.5px}
.proc-title{position:absolute;left:0;right:0;top:24px;text-align:center}
.proc-label{position:absolute;width:90px;text-align:center;font-size:7px;line-height:8px;transform:translateX(-50%)}
.proc-band{position:absolute;left:0;top:234px;width:562px;height:28px;background:var(--blue);color:#fff;font-size:7px;line-height:9px;text-align:center;padding-top:5px}
.cust-title{position:absolute;left:0;right:0;top:56px;text-align:center}
.cust-dark{position:absolute;left:13px;top:111px;width:255px;height:120px;background:var(--dark-box);color:#fff;font-size:10px;line-height:12px;padding:30px 15px 0}
.cust-stat{position:absolute;top:111px;width:133px;height:120px;background:var(--blue);color:#fff;text-align:center}
.cust-stat .cap{height:44px;background:var(--blue-deep);font-size:8px;line-height:9px;padding-top:13px}
.cust-stat .num{font-size:25px;font-weight:700;margin-top:12px}
.cust-stat .sub{font-size:7px;margin-top:4px}
.contact{background:var(--blue)}
.contact-brand{left:0;right:0;top:100px;justify-content:center;color:#fff;font-size:10px}
.contact-title{position:absolute;left:0;right:0;top:188px;text-align:center;color:#fff;font-size:13px}
.contact-row{position:absolute;left:0;right:0;top:222px;display:flex;justify-content:center;gap:22px;color:#fff;font-size:7px;align-items:center}
.contact-row span{display:flex;align-items:center;gap:4px}
</style>
</head>
<body>

<section class="hero">
  <div class="slide hero-slide">
    <svg class="bg" width="562" height="316" viewBox="0 0 562 316">
      <defs><linearGradient id="ph0" x1="0" y1="0" x2="1" y2="1"><stop offset="0" stop-color="#5d6470"/><stop offset=".5" stop-color="#cdd4df"/><stop offset="1" stop-color="#eef1f6"/></linearGradient></defs>
      <polygon points="180,0 562,0 562,316 380,316" fill="url(#ph0)" role="img" aria-label="Photo of a hand signing financial reports"/>
      <polygon points="300,316 562,120 562,316" fill="#6b8bcd" opacity=".95"/>
      <polygon points="180,0 300,316 380,316" fill="#ffffff" opacity=".55"/>
    </svg>
    <div class="brand cover-brand"><span class="dot"></span>Amber Heron</div>
    <h1 class="cover-title">Amber Heron<br>NPL Fund</h1>
    <p class="cover-text">Experience with fund management and asset disposal. Utilizing the clues and hints that borrowers and guarantors leave on the Internet, we can special service assets and collect on them more quickly and maximize return.</p>
    <div class="date-pill">Monday, October 24, 2022</div>
    <div class="copyright">Copyright © 2022 Amber Heron</div>
  </div>
</section>

<!-- Cover light -->
<div class="slide" style="left:28px;top:750px">
  <svg class="bg" width="562" height="316" viewBox="0 0 562 316">
    <defs><linearGradient id="ph1" x1="0" y1="0" x2="1" y2="1"><stop offset="0" stop-color="#5d6470"/><stop offset=".5" stop-color="#cdd4df"/><stop offset="1" stop-color="#eef1f6"/></linearGradient></defs>
    <polygon points="180,0 562,0 562,316 380,316" fill="url(#ph1)" role="img" aria-label="Photo of a hand signing financial reports"/>
    <polygon points="300,316 562,120 562,316" fill="#6b8bcd" opacity=".95"/>
    <polygon points="180,0 300,316 380,316" fill="#ffffff" opacity=".55"/>
  </svg>
  <div class="brand cover-brand"><span class="dot"></span>Amber Heron</div>
  <h1 class="cover-title">Amber Heron<br>NPL Fund</h1>
  <p class="cover-text">Experience with fund management and asset disposal. Utilizing the clues and hints that borrowers and guarantors leave on the Internet, we can special service assets and collect on them more quickly and maximize return.</p>
  <div class="date-pill">Monday, October 24, 2022</div>
  <div class="copyright">Copyright © 2022 Amber Heron</div>
</div>

<!-- Cover dark -->
<div class="slide cover-dark" style="left:609px;top:750px">
  <svg class="bg" width="562" height="316" viewBox="0 0 562 316">
    <defs><linearGradient id="ph2" x1="0" y1="0" x2="1" y2="1"><stop offset="0" stop-color="#9aa7bd"/><stop offset=".5" stop-color="#5c6a86"/><stop offset="1" stop-color="#dfe4ec"/></linearGradient></defs>
    <polygon points="180,0 562,0 562,316 380,316" fill="url(#ph2)" role="img" aria-label="Photo of two business people shaking hands"/>
    <polygon points="180,0 300,316 400,316 200,0" fill="#6b8bcd" opacity=".7"/>
    <polygon points="380,316 562,200 562,316" fill="#e8ecf3" opacity=".7"/>
  </svg>
  <div class="brand cover-brand"><span class="dot"></span>Amber Heron</div>
  <h1 class="cover-title">Amber Heron<br>NPL Fund</h1>
  <p class="cover-text">Experience with fund management and asset disposal. Utilizing the clues and hints that borrowers and guarantors leave on the Internet, we can special service assets and collect on them more quickly and maximize return.</p>
  <div class="date-pill">Monday, October 24, 2022</div>
  <div class="copyright">Copyright © 2022 Amber Heron</div>
</div>

<!-- The Edge -->
<div class="slide" style="left:28px;top:1085px">
  <div class="photo" role="img" aria-label="Photo of a handshake between business partners" style="left:314px;top:0;width:202px;height:266px;background:linear-gradient(150deg,#c5cfdc,#6d7c93 55%,#2f3a4c)"></div>
  <h2 class="head edge-title">The <b>EDGE</b></h2>
  <p class="edge-text">Experience with fund management and asset disposal. Utilizing the clues and hints that borrowers and guarantors leave on the Internet, we can special service assets and collect on them more quickly and maximize return.</p>
  <div class="edge-band">Much of the technology and experience as a team can be attributed to the team’s experience at Brightmoor. The principals were the management team that came on in March <b>2020</b> and grew the business from less than <b>12,000 PPP</b> loans to more than <b>800,000</b>.</div>
  <div class="brand foot-brand"><span class="dot"></span>Amber Heron</div>
  <div class="page-no">PAGE | 3</div>
</div>

<!-- Technology -->
<div class="slide" style="left:609px;top:1085px">
  <h2 class="head tech-title">The <b>TECHNOLOGY</b></h2>
  <div class="photo" role="img" aria-label="Photo of a pen over printed bar charts" style="left:0;top:70px;width:562px;height:102px;background:linear-gradient(100deg,#8f8a86,#e9ecf1 35%,#c7d2e4 65%,#d9b9a7)"></div>
  <div class="tech-text">
    <p>Most lenders and servicers use <b>LedgerOne</b> or <b>NoteDesk</b> and then software like <b>RecoverIQ</b> for collections.</p>
    <p>These software packages fail to address the most important factors which is to analyze the borrower (and the guarantors) to allow for customized collection plans. We use enhanced skip tracing developed during PPP forgiveness and collection efforts with advanced social media logic.</p>
    <p>Finally, we use evolving algorithms to price and purchase NPL portfolios at the correct price.</p>
  </div>
  <div class="brand foot-brand"><span class="dot"></span>Amber Heron</div>
  <div class="page-no">PAGE | 4</div>
</div>

<!-- People -->
<div class="slide" style="left:28px;top:1420px">
  <div class="people-panel" role="img" aria-label="Tinted team portrait photo">The<br><b>PEOPLE</b></div>
  <div class="name-bar solid" style="left:35px;top:170px;width:150px"><h3><b>Henry</b> Walsh</h3><span>Managing Partner, Investment Committee</span></div>
  <ul class="bio" style="left:40px;top:210px;width:145px"><li>More than 20 years of banking experience with several national and regional banks.</li><li>Director of a capital management firm; in less than 5 years achieved 4x AUM and outsized returns managing distressed asset funds. Built a framework for additional funds.</li><li>CEO of Brightmoor.</li></ul>

  <div class="name-bar" style="left:206px;top:35px;width:150px"><h3><b>Daniel</b> Marsh</h3><span>Managing Partner, Investment Committee</span></div>
  <ul class="bio" style="left:211px;top:75px;width:145px"><li>Founder of a law firm in the Southwest which became the first in the country sold to private non-lawyer investors.</li><li>Extensive experience with large transactions, including leading a major state liquidation in 2017. Known for liquidation sales inside bankruptcy. Frequent speaker at national bankruptcy conferences.</li><li>COO of an early web company that first implemented a commercially successful e-commerce campaign. Developer of an associate software suite for nonprofits.</li><li>General Counsel of Brightmoor.</li></ul>

  <div class="name-bar" style="left:206px;top:195px;width:150px"><h3><b>Sam</b> Ortega</h3><span>Chief Operating Officer</span></div>
  <ul class="bio" style="left:211px;top:235px;width:145px"><li>Management Consultant at two global advisory firms.</li><li>Founder of two companies that grew to more than 1,000 employees.</li><li>COO of Brightmoor.</li></ul>

  <div class="name-bar" style="left:377px;top:35px;width:150px"><h3><b>Owen</b> Patel</h3><span>Investment Committee</span></div>
  <ul class="bio" style="left:382px;top:75px;width:145px"><li>CEO of an impact investment company.</li><li>CEO of a regional digital bank.</li><li>Director of a community bank.</li><li>Member of a corporate directors association.</li></ul>

  <div class="name-bar solid" style="left:377px;top:136px;width:150px"><h3><b>Lucas</b> Brenner</h3><span>Director of Credit Analytics</span></div>
  <ul class="bio" style="left:382px;top:176px;width:145px"><li>Product and data specialist with more than 15 years technology and startup experience.</li><li>Founded a communications firm with combined email and chat for customer success teams. Raised $5 million and had more than 40,000 users.</li><li>Led advertising products at a tech network and grew from $7 million to $45 million in revenue over 5 years.</li><li>Advisory board member with a venture firm.</li><li>VP, Products, Brightmoor.</li></ul>
  <div class="brand foot-brand"><span class="dot"></span>Amber Heron</div>
  <div class="page-no">PAGE | 5</div>
</div>

<!-- Market -->
<div class="slide" style="left:609px;top:1420px">
  <div class="market-panel"></div>
  <div class="photo" role="img" aria-label="Photo of a desk with printed charts and a pen" style="left:26px;top:26px;width:511px;height:96px;background:linear-gradient(100deg,#a8adb4,#e6e9ee 40%,#cdd6e4 70%,#48505e)"></div>
  <h2 class="head market-title">The<br>MARKET</h2>
  <p class="market-text">The commercial lending market size was valued at <b>$8,823.53</b> billion in <b>2020</b>, and is projected to reach <b>$29,379.83</b> billion by <b>2030</b>, growing at a CAGR of <b>13.1%</b> from <b>2021</b> to <b>2030</b>.<br><br>Source:<br><a>https://www.examplemarketdata.com/commercial-lending-market</a></p>
  <svg style="position:absolute;left:195px;top:150px" width="220" height="100" viewBox="0 0 220 100">
    <g font-family="Ubuntu,sans-serif" font-size="5" fill="#fff">
      <text x="0" y="6">35000</text><text x="0" y="18">30000</text><text x="0" y="30">25000</text><text x="0" y="42">20000</text><text x="0" y="54">15000</text><text x="0" y="66">10000</text><text x="2" y="78">5000</text><text x="10" y="90">0</text>
    </g>
    <rect x="20" y="2" width="150" height="87" fill="#fff"/>
    <rect x="63" y="68" width="30" height="21" fill="#6b8bcd"/>
    <rect x="103" y="18" width="30" height="71" fill="#3f5ea8"/>
    <g font-family="Ubuntu,sans-serif" font-size="5" fill="#fff"><text x="66" y="75">8823.53</text><text x="106" y="25">29379.83</text><text x="90" y="97">YEAR</text></g>
    <rect x="175" y="42" width="30" height="20" fill="#fff"/>
    <rect x="178" y="46" width="3" height="3" fill="#6b8bcd"/><text x="183" y="49" font-size="4.5" font-family="Ubuntu,sans-serif">2020</text>
    <rect x="178" y="54" width="3" height="3" fill="#3f5ea8"/><text x="183" y="57" font-size="4.5" font-family="Ubuntu,sans-serif">2030</text>
  </svg>
  <p class="market-note">The credit cycle is entering into a period of rising interest rates and corresponding defaults. The fund seeks to take advantage of that emerging opportunity.</p>
  <div class="brand foot-brand"><span class="dot"></span>Amber Heron</div>
  <div class="page-no">PAGE | 6</div>
</div>

<!-- Process -->
<div class="slide" style="left:28px;top:1755px">
  <h2 class="head proc-title">Our <b>PROCESS</b></h2>
  <svg class="bg" width="562" height="316" viewBox="0 0 562 316">
    <rect x="0" y="145" width="562" height="12" fill="#e2e2e2"/>
    <g stroke="#6b8bcd" stroke-width="1">
      <line x1="66" y1="135" x2="66" y2="165"/><line x1="137" y1="130" x2="137" y2="150"/><line x1="208" y1="135" x2="208" y2="165"/><line x1="279" y1="150" x2="279" y2="160"/><line x1="351" y1="135" x2="351" y2="165"/><line x1="422" y1="130" x2="422" y2="150"/><line x1="493" y1="135" x2="493" y2="165"/>
    </g>
    <g fill="#6b8bcd">
      <circle cx="66" cy="135" r="2.5"/><circle cx="208" cy="135" r="2.5"/><circle cx="351" cy="135" r="2.5"/><circle cx="493" cy="135" r="2.5"/>
      <circle cx="137" cy="150" r="2.5"/><circle cx="279" cy="150" r="2.5"/><circle cx="422" cy="150" r="2.5"/>
    </g>
    <g fill="#6b8bcd">
      <circle cx="66" cy="175" r="13"/><circle cx="208" cy="175" r="13"/><circle cx="351" cy="175" r="13"/><circle cx="493" cy="175" r="13"/>
    </g>
    <g fill="#3f5ea8">
      <circle cx="137" cy="125" r="13"/><circle cx="279" cy="125" r="13"/><circle cx="422" cy="125" r="13"/>
    </g>
    <g fill="none" stroke="#fff" stroke-width="1.3">
      <circle cx="60" cy="173" r="3"/><circle cx="72" cy="173" r="3"/><path d="M56 181 q4-5 8 0 M68 181 q4-5 8 0"/>
      <circle cx="208" cy="177" r="5"/><path d="M205 171 h6"/>
      <rect x="345" y="169" width="5" height="5"/><rect x="352" y="169" width="5" height="5"/><rect x="345" y="176" width="5" height="5"/><rect x="352" y="176" width="5" height="5"/>
      <circle cx="493" cy="172" r="4"/><path d="M491 177 v4 h4 v-4"/>
      <ellipse cx="279" cy="125" rx="6" ry="4"/>
      <circle cx="422" cy="125" r="4"/><circle cx="422" cy="125" r="7" stroke-dasharray="2 2"/>
    </g>
    <text x="137" y="129" text-anchor="middle" fill="#fff" font-size="12" font-weight="700" font-family="Ubuntu,sans-serif">$</text>
    <text x="208" y="179" text-anchor="middle" fill="#fff" font-size="6" font-family="Ubuntu,sans-serif">$</text>
  </svg>
  <p class="proc-label" style="left:66px;top:100px">Work with our lender customers on their non-performing loan portfolio.</p>
  <p class="proc-label" style="left:208px;top:85px">Provide special servicing in compliance with bank’s servicing criteria.</p>
  <p class="proc-label" style="left:351px;top:93px">Maintain first right of refusal to purchase loan using proprietary algorithm.</p>
  <p class="proc-label" style="left:493px;top:117px">Liquidation, when necessary.</p>
  <p class="proc-label" style="left:137px;top:195px">Purchase participation in non-performing loans.</p>
  <p class="proc-label" style="left:279px;top:195px">Provide bank access to NPL platform.</p>
  <p class="proc-label" style="left:422px;top:195px">Internal servicing standards.</p>
  <div class="proc-band">Initially partner with licensed collection agencies to supplement our in-house abilities<br>(and comply with regulatory requirements). Potential to acquire and bring completely in-house.</div>
  <div class="brand foot-brand"><span class="dot"></span>Amber Heron</div>
  <div class="page-no">PAGE | 7</div>
</div>

<!-- Customers -->
<div class="slide" style="left:609px;top:1755px">
  <h2 class="head cust-title">Our <b>CUSTOMERS</b></h2>
  <div class="cust-dark">Target Market (It would seem we should narrow the target market and also point out any special relationships, people that Henry can source from last experience or otherwise explain why we have a leg up on pipeline.</div>
  <div class="cust-stat" style="left:272px"><div class="cap">Community<br>Banks</div><div class="num">5,000</div><div class="sub">Nearly</div></div>
  <div class="cust-stat" style="left:408px"><div class="cap">Mid-market<br>Banks</div><div class="num">4,000</div><div class="sub">Approximately</div></div>
  <div class="brand foot-brand"><span class="dot"></span>Amber Heron</div>
  <div class="page-no">PAGE | 8</div>
</div>

<!-- Contact -->
<div class="slide contact" style="left:318px;top:2090px">
  <div class="photo" role="img" aria-label="Faint tinted photo of a desk with documents" style="left:0;top:0;width:562px;height:316px;background:linear-gradient(120deg,#7f9ad3,#6b8bcd 50%,#5f7fc2);opacity:.9"></div>
  <div class="brand contact-brand"><span class="dot"></span>Amber Heron</div>
  <h2 class="contact-title">Contact Us</h2>
  <div class="contact-row">
    <span><svg width="8" height="8" viewBox="0 0 10 10"><path d="M2 1 l2 2 -1 1 q1 2 3 3 l1-1 2 2 -1 1 q-5 0-8-7z" fill="none" stroke="#fff"/></svg>Phone Number Goes Here</span>
    <span><svg width="8" height="8" viewBox="0 0 10 10"><circle cx="5" cy="5" r="4" fill="none" stroke="#fff"/><circle cx="5" cy="5" r="1.5" fill="none" stroke="#fff"/></svg>E-Mail Address Goes Here</span>
    <span><svg width="8" height="8" viewBox="0 0 10 10"><circle cx="5" cy="5" r="4" fill="none" stroke="#fff"/><path d="M1 5h8M5 1v8" stroke="#fff"/></svg>URL Address Goes Here</span>
  </div>
</div>

</body>
</html>
```